Velvet Pressings Techno Label Business Card

I'm looking for a very clean business card for my Velvet Pressings music label. The label focusses on techno music. The card should include:

• my name : Bram Quintel as "Founder & CEO"
• email address: bram@velvet-pressings.example
• web: www.velvet-pressings.example
• facebook logo + /velvetpress
• twitter logo + /velvetpress
• soundcloud logo + /velvetpressings

Feel free to include your ideas! I'm looking forward to discuss about it.

Bram

Industry/Entity Type

Business

Contact Information for Business Card

I don't like glossy cards. Prefer matt.

Requirements
Nice to have
• Maybe on one side the complete logo, other side just the icon.
Should not have
• Flashy stuff. Must be clean and business like style.

```html
<!DOCTYPE html>
<html lang="en">
<head>
<meta charset="utf-8">
<title>Velvet Pressings – Business Card</title>
<link rel="stylesheet" href="https://fonts.googleapis.com/css2?family=Arimo:wght@400;700&display=swap">
<style>
  :root {
    --orange: #e8621c;
    --grey-text: #7a7a7a;
    --card-paper: #ecebe8;
    --backdrop: #d9d9d7;
  }
  * { margin: 0; padding: 0; box-sizing: border-box; }
  html, body {
    width: 1200px;
    height: 1000px;
    overflow: hidden;
    background: var(--backdrop);
    font-family: "Arimo", Arial, sans-serif;
  }
  .canvas {
    position: relative;
    width: 1200px;
    height: 1000px;
  }
  .card {
    position: absolute;
    left: 300px;
    width: 600px;
    height: 340px;
    background: var(--card-paper);
    overflow: hidden;
    box-shadow: 0 2px 6px rgba(0,0,0,0.15);
  }
  .card--contact { top: 120px; }
  .card--brand { top: 540px; }

  .band {
    position: absolute;
    left: 0;
    width: 100%;
    height: 12px;
    background: var(--orange);
  }
  .band--top { top: 0; }
  .band--bottom { bottom: 14px; }

  /* contact side */
  .accent-disc {
    position: absolute;
    left: -110px;
    top: 20px;
    width: 300px;
    height: 300px;
  }
  .contact-block {
    position: absolute;
    right: 40px;
    top: 92px;
    width: 270px;
  }
  .contact-name {
    font-weight: 700;
    font-size: 21px;
    color: var(--orange);
    letter-spacing: 0.5px;
    padding-bottom: 4px;
    border-bottom: 2px solid var(--orange);
  }
  .contact-role {
    margin-top: 6px;
    text-align: right;
    font-weight: 700;
    font-size: 14px;
    color: var(--orange);
    letter-spacing: 0.5px;
  }
  .contact-email {
    position: absolute;
    right: 40px;
    top: 196px;
    font-size: 17px;
    color: var(--grey-text);
    letter-spacing: 0.3px;
  }
  .social-list {
    position: absolute;
    right: 40px;
    top: 236px;
    display: flex;
    gap: 18px;
    list-style: none;
  }
  .social-item {
    display: flex;
    align-items: center;
    gap: 6px;
    font-size: 14px;
    color: var(--grey-text);
    letter-spacing: 0.3px;
  }
  .social-dot {
    width: 12px;
    height: 12px;
    border-radius: 50%;
    background: var(--orange);
  }

  /* brand side */
  .brand-lockup {
    position: absolute;
    left: 50px;
    top: 110px;
    display: flex;
    align-items: center;
    gap: 18px;
  }
  .brand-dot {
    width: 64px;
    height: 64px;
    border-radius: 50%;
    background: var(--orange);
  }
  .brand-name {
    font-weight: 700;
    font-size: 50px;
    color: var(--grey-text);
    letter-spacing: 0.5px;
  }
  .brand-web {
    position: absolute;
    left: 0;
    width: 100%;
    top: 250px;
    text-align: center;
    font-size: 20px;
    color: var(--orange);
    letter-spacing: 0.5px;
  }
</style>
</head>
<body>
<main class="canvas">
  <section class="card card--contact" aria-label="Business card, contact side">
    <div class="band band--top"></div>
    <svg class="accent-disc" viewBox="0 0 300 300" aria-hidden="true">
      <circle cx="150" cy="150" r="150" fill="var(--orange)"/>
    </svg>
    <div class="contact-block">
      <p class="contact-name">Bram Quintel</p>
      <p class="contact-role">Founder &amp; CEO</p>
    </div>
    <p class="contact-email">bram@velvet-pressings.example</p>
    <ul class="social-list">
      <li class="social-item"><span class="social-dot" aria-hidden="true"></span>/velvetpress</li>
      <li class="social-item"><span class="social-dot" aria-hidden="true"></span>/velvetpress</li>
      <li class="social-item"><span class="social-dot" aria-hidden="true"></span>/velvetpressings</li>
    </ul>
    <div class="band band--bottom"></div>
  </section>

  <section class="card card--brand" aria-label="Business card, brand side">
    <div class="band band--top"></div>
    <div class="brand-lockup">
      <span class="brand-dot" aria-hidden="true"></span>
      <span class="brand-name">Velvet Pressings</span>
    </div>
    <p class="brand-web">www.velvet-pressings.example</p>
    <div class="band band--bottom"></div>
  </section>
</main>
</body>
</html>
```